Real Estate Webpage Design

We have an existing website: brindlewoodhomes.com.au
We focus customised service mainly on Property Management and second-hand property sales.
We are not entirely happy about the current design and layout can stay roughly the same as the back end coding is linked to a CRM system.
We would like to see the design are more reachable to our clients and appearing.
Please check our Website Design Draft for more details.

Industry/Entity Type

Real estate Agency

Number of Pages Required

5+ page

Font styles to use
Sans Serif

Colors

Designer to choose colors to be used in the design.

```html
<!DOCTYPE html>
<html lang="en">
<head>
<meta charset="utf-8">
<title>Brindlewood Homes – Real Estate</title>
<link href="https://fonts.googleapis.com/css2?family=Hind:wght@400;500;600;700&display=swap" rel="stylesheet">
<style>
:root{
  --yellow:#f8b81c;
  --dark:#1f2531;
  --ink:#1b1b1b;
  --grey:#666;
  --white:#fff;
}
*{margin:0;padding:0;box-sizing:border-box}
html,body{width:1200px;height:3513px;overflow:hidden}
body{font-family:"Hind",sans-serif;color:var(--ink);background:#fff;position:relative}
.abs{position:absolute}
svg{display:block}

/* header */
.header{position:absolute;left:0;top:0;width:1200px;height:146px;background:#fff}
.brand{position:absolute;left:104px;top:62px;width:180px;text-align:center;color:var(--dark)}
.brand .name{font-size:29px;font-weight:600;line-height:1;display:flex;align-items:center;justify-content:center;gap:7px}
.brand .dot{width:11px;height:11px;background:var(--yellow);border-radius:50%;flex:none}
.brand .sub{display:block;font-size:10px;font-weight:500;color:var(--yellow);margin-top:6px}
.contacts{position:absolute;left:377px;top:14px;display:flex}
.contact{display:flex;align-items:center;gap:10px;font-size:13.5px;font-weight:500;line-height:1.45;white-space:nowrap}
.contact .ic{width:40px;height:40px;border-radius:50%;border:2px solid var(--dark);background:var(--yellow);display:flex;align-items:center;justify-content:center;flex:none}
.navbar{position:absolute;left:300px;top:74px;width:900px;height:72px;background:var(--dark)}
.navbar:before{content:"";position:absolute;left:-12px;top:0;width:40px;height:72px;background:var(--yellow);transform:skewX(-35deg);z-index:-1}
.navbar .stripe{position:absolute;left:0;top:-4px;width:900px;height:4px;background:var(--yellow)}
.nav{position:absolute;left:54px;top:0;height:72px;display:flex;align-items:center;gap:37px;color:#fff;font-size:17px;font-weight:500}
.nav .lang{width:32px;height:32px;border-radius:50%;background:var(--yellow)}

/* hero */
.hero{position:absolute;left:0;top:146px;width:1200px;height:560px;background:linear-gradient(100deg,#3d4650 0%,#6c7a86 45%,#c8d2dc 75%,#9aa8b4 100%)}
.hero-text{position:absolute;left:110px;top:146px;color:#fff;width:620px}
.hero-text .pre{font-size:21px;font-weight:600;margin-top:145px}
.hero-text h1{font-size:39px;font-weight:600;line-height:1.2;margin-top:2px;white-space:nowrap}
.hero-text p{font-size:14px;line-height:1.85;margin-top:10px;width:430px}
.btn{display:inline-block;background:var(--yellow);color:var(--ink);font-weight:600;border-radius:6px}
.hero-text .btn{font-size:21px;padding:12px 22px 8px 28px;margin-top:20px}

/* schedule */
.schedule{position:absolute;left:0;top:630px;width:1200px;height:158px}
.schedule h2{position:absolute;left:0;width:1200px;top:28px;text-align:center;font-size:24px;font-weight:700}
.field{position:absolute;top:78px;width:193px;height:55px;background:#fff;border-radius:5px;font-size:14px;font-weight:600;padding:21px 0 0 23px}
.submit{position:absolute;top:78px;left:862px;width:168px;height:55px;background:var(--dark);color:#fff;border-radius:6px;text-align:center;font-weight:700;font-size:16px;padding-top:18px}

/* section titles */
.title{position:absolute;left:0;width:1200px;text-align:center;font-size:36px;font-weight:500}
.title span{color:var(--yellow)}
.divider{position:absolute;left:0;width:1200px;display:flex;justify-content:center;align-items:center;gap:8px}
.divider i{width:70px;height:2px;background:var(--ink)}
.divider b{width:10px;height:10px;border:2px solid var(--yellow)}

/* listings */
.tabs{position:absolute;top:966px;left:0;width:1200px;display:flex;justify-content:center;font-size:20px;color:#555;font-weight:500}
.tabs div{padding:10px 17px 6px;margin:0 40px}
.tabs .on{background:#fff;color:var(--ink);box-shadow:0 2px 10px rgba(0,0,0,.12);border-radius:4px;font-weight:600}
.card{position:absolute;top:1049px;width:292px;height:332px;background:#fff;box-shadow:0 4px 14px rgba(0,0,0,.15);border-radius:6px;overflow:hidden}
.card .photo{height:252px;position:relative}
.card .tag{position:absolute;left:18px;top:22px;background:#fff;border-radius:4px;padding:6px 12px 3px;font-size:15px;font-weight:500}
.card .go{position:absolute;right:17px;bottom:17px;width:30px;height:30px;border-radius:50%;background:#fff;border:1px solid #333;display:flex;align-items:center;justify-content:center}
.card .row{display:flex;justify-content:space-between;padding:16px 18px 0;font-size:17px;font-weight:500}
.card .price{color:var(--yellow)}
.card .meta{display:flex;justify-content:space-between;padding:6px 18px;font-size:11px;color:#555}
.card .stars{color:var(--yellow);font-size:13px;letter-spacing:1px}

/* about */
.about{position:absolute;left:0;top:1480px;width:1200px;height:594px;background:linear-gradient(90deg,#2c3240,#3a4150)}
.about .photo{position:absolute;left:112px;top:95px;width:393px;height:389px;background:linear-gradient(135deg,#5d6878,#e2e6ec 60%,#8a93a0)}
.about .copy{position:absolute;left:571px;top:82px;width:520px;color:#fff}
.about h2{font-size:36px;font-weight:600}
.about .divider{position:static;justify-content:flex-start;margin:6px 0 14px}
.about .divider i{background:#fff}
.about p{font-size:16.5px;line-height:1.65;margin-bottom:27px}
.about .btn{font-size:20px;padding:12px 24px 8px 30px;margin-top:-2px}

/* team */
.member{position:absolute;top:2302px;width:240px;text-align:center}
.member .avatar{width:116px;height:116px;border-radius:50%;margin:0 auto;border:3px solid var(--yellow);background:linear-gradient(#e4e4e4,#9a9a9a)}
.member .name{font-size:20px;font-weight:600;margin-top:9px}
.member .name small{font-size:16px;font-weight:500}
.member .icons{display:flex;justify-content:center;gap:14px;margin-top:6px}
.member .icons i{width:22px;height:22px;border-radius:50%;background:var(--dark)}
.arrow{position:absolute;top:2366px;width:30px;height:30px;border-radius:50%;background:var(--dark);display:flex;align-items:center;justify-content:center}

/* testimonial */
.testi{position:absolute;left:0;top:2557px;width:1200px;height:500px}
.testi h2{position:absolute;left:0;width:1200px;top:77px;text-align:center;font-size:36px;font-weight:700}
.testi p{position:absolute;left:190px;width:820px;top:185px;text-align:center;font-size:16.5px;line-height:1.66;color:#333}
.testi .face{position:absolute;left:573px;top:331px;width:54px;height:54px;border-radius:50%;border:3px solid var(--dark);background:linear-gradient(#8b9a7f,#4c5a4a)}
.testi .who{position:absolute;left:0;width:1200px;top:407px;text-align:center;font-size:20px;font-weight:500}

/* footer */
.footer{position:absolute;left:0;top:3055px;width:1200px;height:458px;background:var(--dark);color:#fff}
.col{position:absolute;top:88px}
.col h4{font-size:20px;font-weight:600;margin-bottom:16px}
.col li{list-style:none;font-size:14.5px;line-height:40px;display:flex;align-items:center;gap:6px}
.col li:before{content:"→";color:var(--yellow);font-weight:700}
.col.contact-us li:before{content:none}
.col.contact-us li{line-height:24px;margin-bottom:20px;align-items:flex-start}
.col.contact-us li b{color:var(--yellow);width:16px;flex:none}
.fbrand{position:absolute;left:900px;top:132px;font-size:34px;font-weight:600;display:flex;align-items:center;gap:8px}
.fbrand .dot{width:12px;height:12px;background:var(--yellow);border-radius:50%}
.follow{position:absolute;left:903px;top:232px;font-size:14px;font-weight:600}
.social{position:absolute;left:903px;top:267px;display:flex;gap:22px}
.social i{width:30px;height:30px;border-radius:50%;background:var(--yellow)}
.rule{position:absolute;left:110px;top:369px;width:980px;height:1px;background:#fff}
.copy-line{position:absolute;left:0;width:1200px;top:405px;text-align:center;font-size:14px}
</style>
</head>
<body>

<header class="header">
  <div class="brand">
    <div class="name"><span class="dot"></span>Brindlewood</div>
    <span class="sub">Homes Group</span>
  </div>
  <div class="contacts">
    <div class="contact" style="width:238px"><span class="ic"><svg width="16" height="16" viewBox="0 0 24 24"><path d="M6 3l4 4-2 3c1 2 3 4 6 6l3-2 4 4-3 3C10 20 4 14 3 6z" fill="#1f2531"/></svg></span><div>Call Now:<br>02 6000 3172</div></div>
    <div class="contact" style="width:238px"><span class="ic"><svg width="16" height="14" viewBox="0 0 24 20"><rect x="1" y="2" width="22" height="16" fill="#1f2531"/><path d="M1 2l11 9 11-9" stroke="#f8b81c" stroke-width="2" fill="none"/></svg></span><div>Mail Us:<br>info@brindlewoodhomes.com.au</div></div>
    <div class="contact"><span class="ic"><svg width="14" height="18" viewBox="0 0 14 20"><path d="M7 0a7 7 0 017 7c0 5-7 13-7 13S0 12 0 7a7 7 0 017-7z" fill="#1f2531"/><circle cx="7" cy="7" r="2.5" fill="#f8b81c"/></svg></span><div>Location:<br>18/4 Marlow Street, Harcourt</div></div>
  </div>
  <nav class="navbar">
    <div class="stripe"></div>
    <div class="nav"><span>Home</span><span>About Us</span><span>Leasing</span><span>Buy</span><span>Sell</span><span>Our Team</span><span>Blog</span><span>Contact Us</span><span class="lang"></span></div>
  </nav>
</header>

<section class="hero" role="img" aria-label="Photo of a modern white apartment building under a blue sky"></section>
<div class="hero-text">
  <div class="pre">Welcome To</div>
  <h1>Brindlewood – a place called home</h1>
  <p>Brindlewood means “the home, the house”, buying a property is one of the most expensive expenses and important assets for people.</p>
  <span class="btn">Get Started</span>
</div>

<section class="schedule">
  <svg class="abs" style="left:0;top:0" width="1200" height="158"><path d="M0 48 L420 48 Q600 -12 780 48 L1200 48 L1200 158 L0 158Z" fill="#f8b81c"/></svg>
  <h2>Schedule A Service Now</h2>
  <div class="field" style="left:168px">Name*</div>
  <div class="field" style="left:395px">Email*</div>
  <div class="field" style="left:622px">Phone Number*</div>
  <div class="submit">SUBMIT</div>
</section>

<h2 class="title" style="top:868px">This Month At <span>Brindlewood Homes Group</span></h2>
<div class="divider" style="top:932px"><i></i><b></b><i></i></div>
<div class="tabs"><div>For Sale</div><div class="on">For Lease</div><div>Open Times</div><div>Sold</div><div>Leased</div></div>

<div class="card" style="left:112px">
  <div class="photo" role="img" aria-label="Photo of a two-storey house with a double garage" style="background:linear-gradient(#7fa6d6,#c9c7c2 55%,#a8988a)"><span class="tag">⚲ Red Hill</span><span class="go">→</span></div>
  <div class="row"><span>Red Hill</span><span class="price">$ 1400 pw</span></div>
  <div class="meta"><span>▭ 04 &nbsp; ⌂ 02 &nbsp; ▣ 02</span><span class="stars">★★★★★</span></div>
</div>
<div class="card" style="left:454px">
  <div class="photo" role="img" aria-label="Photo of an apartment living room with a patterned sofa" style="background:linear-gradient(#dfe2e4,#b7b4ae 60%,#7b5a3e)"><span class="tag">⚲ Braddon</span><span class="go">→</span></div>
  <div class="row"><span>Braddon</span><span class="price">$ 560 pw</span></div>
  <div class="meta"><span>▭ 01 &nbsp; ⌂ 01 &nbsp; ▣ 01</span><span class="stars">★★★★★</span></div>
</div>
<div class="card" style="left:796px">
  <div class="photo" role="img" aria-label="Photo of a single-storey brick house with a garden" style="background:linear-gradient(#3b7fd9,#9db7d6 45%,#8c7a66 70%,#b8b0a4)"><span class="tag">⚲ Griffith</span><span class="go">→</span></div>
  <div class="row"><span>Griffith</span><span class="price">$ 1300 pw</span></div>
  <div class="meta"><span>▭ 04 &nbsp; ⌂ 02 &nbsp; ▣ 03</span><span class="stars">★★★★★</span></div>
</div>

<section class="about">
  <div class="photo" role="img" aria-label="Photo of a modern house facade"></div>
  <div class="copy">
    <h2>About Brindlewood</h2>
    <div class="divider"><i></i><b></b><i></i></div>
    <p>Brindlewood stands for “the home, the house”, buying a property is one of the most expensive expenses and important assets for people. Brindlewood is a real estate company located in Harcourt, Canberra.</p>
    <p>Being a portfolio sales agent and property manager, coupled with our high-profile international real estate experience, Brindlewood is considered a market leader on the cutting edge with deep industry knowledge.</p>
    <span class="btn">Read More</span>
  </div>
</section>

<h2 class="title" style="top:2158px">Our <span>Team</span></h2>
<div class="divider" style="top:2221px"><i style="width:32px"></i><b></b><i style="width:32px"></i></div>
<span class="arrow" style="left:36px"><svg width="14" height="14" viewBox="0 0 14 14"><path d="M13 7H2M6 2L1 7l5 5" stroke="#fff" stroke-width="2.4" fill="none"/></svg></span>
<span class="arrow" style="left:1135px"><svg width="14" height="14" viewBox="0 0 14 14"><path d="M1 7h11M8 2l5 5-5 5" stroke="#fff" stroke-width="2.4" fill="none"/></svg></span>
<div class="member" style="left:79px"><div class="avatar" role="img" aria-label="Portrait photo of the principal"></div><div class="name">Leon Hart <small>(Principal)</small></div><div class="icons"><i></i><i></i><i></i></div></div>
<div class="member" style="left:342px"><div class="avatar" role="img" aria-label="Portrait photo of a manager"></div><div class="name">Nora Vale <small>(Manager)</small></div><div class="icons"><i></i><i></i><i></i></div></div>
<div class="member" style="left:607px"><div class="avatar" role="img" aria-label="Portrait photo of a manager"></div><div class="name">Tessa Moor <small>(Manager)</small></div><div class="icons"><i></i><i></i><i></i></div></div>
<div class="member" style="left:869px"><div class="avatar" role="img" aria-label="Portrait photo of an assistant"></div><div class="name">Ivy Lane <small>(Assistant)</small></div><div class="icons"><i></i><i></i><i></i></div></div>

<section class="testi">
  <svg class="abs" style="left:0;top:0" width="1200" height="500"><defs><linearGradient id="tg" x1="0" x2="1"><stop offset="0" stop-color="#f8c02a"/><stop offset="1" stop-color="#e9ad1a"/></linearGradient></defs><path d="M0 60 L600 0 L1200 60 L1200 500 L0 500Z" fill="url(#tg)"/></svg>
  <h2>What Customer Says</h2>
  <div class="divider" style="top:133px"><i></i><b></b><i></i></div>
  <p>They are a greatly professional, organized and experienced team with extensive knowledge and understanding of the local market. My husband and I were provided with excellent feedback in a simple language we could understand and advice throughout the house journey and we were very pleased with the results. We highly recommend Brindlewood Homes group to anyone buying, selling or in need of property management in the local area.</p>
  <div class="face" role="img" aria-label="Small photo of the client's home"></div>
  <div class="who">Rosa Bellamy, Thanks Brindlewood</div>
</section>

<footer class="footer">
  <div class="col" style="left:109px"><h4>Quick Links</h4><ul><li>Home</li><li>About</li><li>Lease</li><li>Testimonials</li><li>Contact</li></ul></div>
  <div class="col" style="left:282px"><h4>Services</h4><ul><li>Sold</li><li>Buy</li><li>Open Times</li><li>For sale</li><li>For Lease</li></ul></div>
  <div class="col" style="left:472px"><h4>Help Links</h4><ul><li>FAQ</li><li>Terms</li><li>Privacy</li><li>Policy</li><li>Conditions</li></ul></div>
  <div class="col contact-us" style="left:659px"><h4>Contact us</h4><ul>
    <li><b>⚲</b>18/4 Marlow Street,<br>Harcourt, ACT, 2900</li>
    <li><b>✉</b>info@brindlewoodhomes.com.au</li>
    <li><b>✆</b>02 6000 3172</li>
    <li><b>▤</b>02 6000 3190</li></ul></div>
  <div class="fbrand"><span class="dot"></span>Brindlewood</div>
  <div class="follow">Follow Us On:</div>
  <div class="social"><i></i><i></i><i></i><i></i></div>
  <div class="rule"></div>
  <div class="copy-line">Copyrights@2022.Brindlewood.All Rights Reserved</div>
</footer>

</body>
</html>
```